Business Card & Logo Design Project

I am looking for a slick/simple design for a logo and business card, for a music Producer/Mixer/Engineer.

I'm based in Tokyo, Japan and I help my clients polish up their creation to major radio/TV status. My clients pay me for my taste, sense of balance expertise and creative direction/

Design should give impression of seal of quality, professionalism, and enthusiasm need some sort of a logo like design for "vantrix productions".

Please don't include music notes or instruments or anything musically related and anything samurai or ninja or too much Japan in them on the design.

I like clever, slick stuff that's not too obvious.
I also like a smooth gradation type transition. My favorite color is deep dark blue/

Good Luck and Thank you for your effort.
Updates

I would like a two-sided design for this one.
One side with "vantrix productions" (all lower case) on, and the other side with my name and contact info.

Please also consider portrait position (or direction).  (as opposed to landscape) 

Target Market(s)

My primary targets are artists & bands, who want absolute best for their creation.

Industry/Entity Type

Business

Requirements
Must have
• Two-Sided
1, vantrix productions
2, Kenji Harumoto, Producer/Mixer/Engineer, +81 090 4827 3516, brambleway@mailnest.example
Nice to have
• Any suggestions are welcome//
Should not have
• Anything music related images.
(e.g. CD, music notations, instruments etc.)

```html
<!DOCTYPE html>
<html lang="en">
<head>
<meta charset="utf-8">
<title>vantrix productions — business cards</title>
<link href="https://fonts.googleapis.com/css2?family=Bodoni+Moda:wght@400;500&display=swap" rel="stylesheet">
<style>
  :root {
    --ink: #0b0b0b;
    --band: #2a2ad6;
    --aqua: #80f6f6;
    --edge: #b79ad6;
    --paper: #ffffff;
    --white-type: #f4efec;
    --sky-type: #4d8fe0;
    --logo-deep: #2b3bcc;
    --logo-light: #86daf2;
  }
  * { margin: 0; padding: 0; box-sizing: border-box; }
  html, body { width: 1200px; height: 921px; overflow: hidden; background: var(--paper); }
  body { position: relative; font-family: "Bodoni Moda", "Didot", serif; }

  .card { position: absolute; border-radius: 24px; overflow: hidden; }
  .card-bg { position: absolute; inset: 0; width: 100%; height: 100%; display: block; }

  .card--front-light { left: 0;   top: 0;   width: 570px; height: 368px; }
  .card--back-light  { left: 602px; top: 0; width: 598px; height: 362px; }
  .card--front-sky   { left: 9px;  top: 540px; width: 567px; height: 360px; }
  .card--back-sky    { left: 629px; top: 533px; width: 571px; height: 363px; }

  .wordmark { position: absolute; display: flex; align-items: center; gap: 14px; white-space: nowrap; }
  .wordmark-dot { border-radius: 50%; flex: none; }
  .wordmark-name { font-weight: 400; letter-spacing: 0.5px; }

  .wordmark--large { left: 30px; top: 118px; }
  .wordmark--large .wordmark-dot { width: 62px; height: 62px; }
  .wordmark--large .wordmark-name { font-size: 38px; line-height: 1.08; display: flex; flex-direction: column; }

  .wordmark--small { right: 26px; bottom: 22px; gap: 8px; }
  .wordmark--small .wordmark-dot { width: 22px; height: 22px; }
  .wordmark--small .wordmark-name { font-size: 19px; }

  .tone-white .wordmark-dot { background: var(--white-type); }
  .tone-white .wordmark-name { color: var(--white-type); }
  .tone-light .wordmark-dot { background: var(--logo-light); }
  .tone-light .wordmark-name { color: var(--logo-light); }
  .tone-deep .wordmark-dot { background: var(--logo-deep); }
  .tone-deep .wordmark-name { color: var(--logo-deep); }

  .contact { position: absolute; left: 28px; top: 20px; }
  .contact-name { font-size: 39px; font-weight: 400; line-height: 1.1; letter-spacing: 0.5px; }
  .contact-role { font-size: 25px; line-height: 1.2; margin-top: 2px; }
  .contact-line { font-size: 21px; line-height: 1.2; }
  .contact-phone { margin-top: 40px; }
  .contact-email { margin-top: 42px; }

  .contact--white { color: var(--white-type); }
  .contact--sky { color: var(--sky-type); font-weight: 500; }
</style>
</head>
<body>

<svg width="0" height="0" style="position:absolute" aria-hidden="true">
  <defs>
    <symbol id="card-face" viewBox="0 0 500 320" preserveAspectRatio="none">
      <rect x="0" y="0" width="500" height="320" fill="var(--aqua)"/>
      <path d="M376 0 H426 C396 150 330 262 168 320 C300 262 356 150 376 0 Z" fill="var(--band)"/>
      <path d="M0 0 H376 C356 150 300 262 168 320 H0 Z" fill="var(--ink)"/>
      <rect x="0.75" y="0.75" width="498.5" height="318.5" rx="21" ry="21" fill="none" stroke="var(--edge)" stroke-width="1.5" vector-effect="non-scaling-stroke"/>
    </symbol>
  </defs>
</svg>

<section class="card card--front-light">
  <svg class="card-bg" aria-hidden="true"><use href="#card-face" width="100%" height="100%"/></svg>
  <div class="wordmark wordmark--large tone-white">
    <span class="wordmark-dot"></span>
    <span class="wordmark-name"><span>vantrix</span><span>productions</span></span>
  </div>
</section>

<section class="card card--back-light">
  <svg class="card-bg" aria-hidden="true"><use href="#card-face" width="100%" height="100%"/></svg>
  <div class="contact contact--white">
    <h1 class="contact-name">Kenji Harumoto</h1>
    <p class="contact-role">Producer | Mixer | Engineer</p>
    <p class="contact-line contact-phone">(+81) 090 4827 3516</p>
    <p class="contact-line contact-email">brambleway@mailnest.example</p>
  </div>
  <div class="wordmark wordmark--small tone-deep">
    <span class="wordmark-dot"></span>
    <span class="wordmark-name">vantrix productions</span>
  </div>
</section>

<section class="card card--front-sky">
  <svg class="card-bg" aria-hidden="true"><use href="#card-face" width="100%" height="100%"/></svg>
  <div class="wordmark wordmark--large tone-light">
    <span class="wordmark-dot"></span>
    <span class="wordmark-name"><span>vantrix</span><span>productions</span></span>
  </div>
</section>

<section class="card card--back-sky">
  <svg class="card-bg" aria-hidden="true"><use href="#card-face" width="100%" height="100%"/></svg>
  <div class="contact contact--sky">
    <h2 class="contact-name">Kenji Harumoto</h2>
    <p class="contact-role">Producer | Mixer | Engineer</p>
    <p class="contact-line contact-phone">(+81) 090 4827 3516</p>
    <p class="contact-line contact-email">brambleway@mailnest.example</p>
  </div>
  <div class="wordmark wordmark--small tone-deep">
    <span class="wordmark-dot"></span>
    <span class="wordmark-name">vantrix productions</span>
  </div>
</section>

</body>
</html>
```